finlo-welt.de
Zielgruppe
Alle die kein Geld haben :-)
Aufgabenstellung
Unter finlo-welt.de sollen Informationen rund um Kredite, Kreditkarten, Bonvia usw. entstehen. Diese werden dann unter Subdomains wir konto.finlo-welt.de oder kreditkarte.finlo-welt.de laufen. Die Domain finlo-welt.de soll die Hauptdomain werden wofür ein Logo und ein Layout benötigt wird. Auf den einzelnen Seiten sollen später Reporte verkauft werden und relativ viel mit Plunko Werbung gearbeitet werden. Hier ein paar Beipspiele www.zahlwerk-mohnel.biz, www.lumvesta88.de, www.tanne-blau-heft.de, www.nordlicht-mappe-brief.de
Die genannten Seiten sind keine Meisterleistung in Design und sollen nur in etwa Inhalte und die Einbindung von Plunko Adbox wieder geben. Menüpunkte sind immer gleich und werden sein mit den Untertiteln wie bei www.zahlwerk-mohnel.biz.

```html
<!DOCTYPE html>
<html lang="de">
<head>
<meta charset="utf-8">
<title>finlo-welt.de</title>
<link href="https://fonts.googleapis.com/css2?family=EB+Garamond:wght@400&family=Noto+Sans:wght@400;700&display=swap" rel="stylesheet">
<style>
:root{
  --page:#ffffff;
  --text:#7a7a7a;
  --nav-text:#8a8a8a;
  --green:#5d9f1c;
  --wave:#e6f2da;
  --ad-title:#222222;
  --ad-text:#555555;
  --line:#dcdcdc;
  --logo:#8c8c8c;
  --cover-top:#c4c4c4;
  --cover-bottom:#f6f6f6;
}
*{margin:0;padding:0;box-sizing:border-box}
html,body{width:1200px;height:900px;overflow:hidden;background:var(--page)}
body{position:relative;font-family:"EB Garamond",serif;color:var(--text)}

.site{position:absolute;left:214px;top:0;width:820px;height:900px;
  background:linear-gradient(#ffffff 0,#f4f4f4 420px,#fbfbfb 900px);
  box-shadow:0 0 14px rgba(0,0,0,.12)}
.header{position:absolute;left:0;top:0;width:820px;height:125px;
  background:linear-gradient(#ffffff,#f0f0f0)}
.header svg{position:absolute;left:0;top:0}
.brand{position:absolute;left:548px;top:40px;font-size:40px;color:var(--logo)}

.nav{position:absolute;left:0;top:125px;width:820px;height:48px;display:flex;
  border-top:1px solid var(--line);border-bottom:1px solid var(--line);background:#fff}
.nav a{display:block;text-align:center;padding-top:11px;font-size:18px;color:var(--nav-text);
  text-decoration:none;border-right:1px solid var(--line);height:46px;white-space:nowrap}
.nav a:last-child{border-right:none}
.nav a.active{background:linear-gradient(#e2e2e2,#f7f7f7)}

h1,h2{font-weight:400;color:var(--green)}
.welcome{position:absolute;left:25px;top:190px;width:335px}
.welcome h1{font-size:23px;margin-bottom:4px}
.welcome p{font-size:18.5px;line-height:20px}

.help{position:absolute;left:484px;top:420px;width:318px;text-align:right}
.help h2{font-size:23px;margin-bottom:2px}
.help p{font-size:18.5px;line-height:20px;margin-bottom:18px}

.cover{position:absolute;left:229px;top:466px;width:225px;height:400px;
  background:linear-gradient(var(--cover-top) 0,#d4d4d4 60%,var(--cover-bottom) 100%)}

.adbox{position:absolute;font-family:"Noto Sans",sans-serif}
.adlabel{position:absolute;left:0;top:0;width:100%;display:flex;align-items:center;
  justify-content:space-between;font-size:12px;color:#444}
.adlabel .go{width:17px;height:16px;background:#222;display:flex;align-items:center;justify-content:center}
.ad{position:absolute;left:0;width:100%}
.ad-title{font-size:15.5px;font-weight:700;color:var(--ad-title);text-decoration:underline;
  line-height:19px;letter-spacing:.2px}
.ad-text{font-size:14px;color:var(--ad-text);line-height:19px;letter-spacing:.9px}
.ad-url{font-size:11.5px;color:#111;letter-spacing:.4px;white-space:nowrap;overflow:hidden}

.side{left:20px;top:128px;width:180px;height:700px}
.mid{left:243px;top:434px;width:182px;height:300px}
.top-label{left:812px;top:217px;width:183px;height:20px}
.top-ad{top:252px;width:182px;height:120px}
</style>
</head>
<body>

<aside class="adbox side">
  <div class="adlabel"><span>Plunko-Anzeigen</span><span class="go"><svg width="9" height="10"><path d="M1 0 L9 5 L1 10 Z" fill="#fff"/></svg></span></div>
  <div class="ad" style="top:33px"><div class="ad-title">1. Kredit-Anfrage in 5min</div><div class="ad-text">2. Angebot in Ruhe prüfen 3. auf Wunsch abschließen</div><div class="ad-url">kreditwabe.com/ohneBonvia</div></div>
  <div class="ad" style="top:160px"><div class="ad-title">Goldene Karte ohne Bonvia</div><div class="ad-text">Echte hochgeprägte Velancard keine Ablehnung möglich! Sofort</div><div class="ad-url">www.karte-morvel.eu</div></div>
  <div class="ad" style="top:324px"><div class="ad-title">1. Antrag ausfüllen</div><div class="ad-text">2. Angebot prüfen 3. Schuldenfrei werden</div><div class="ad-url">www.jetzt-tilgafix.com</div></div>
  <div class="ad" style="top:431px"><div class="ad-title">Billiger Kredit ab 3,45%</div><div class="ad-text">Kredite: für 10.000€ ab 129€/Monat! Alle Kredite kostenlos im Vergleich</div><div class="ad-url">www.Kravento.de/Kredite-Vergleich</div></div>
  <div class="ad" style="top:567px"><div class="ad-title">Raus aus den Schulden</div><div class="ad-text">Schuldenfrei in 4 Jahren. Sofort Kostenlose Schuldnerberatung</div><div class="ad-url">www.beratung-holmtal.de</div></div>
</aside>

<main class="site">
  <header class="header">
    <svg width="820" height="125" aria-hidden="true">
      <path d="M0 20 C150 70 300 90 440 60 C540 40 600 20 700 30 L700 45 C600 40 540 62 440 82 C300 112 150 95 0 50 Z" fill="var(--wave)"/>
    </svg>
    <div class="brand">finlo-welt.de</div>
  </header>
  <nav class="nav">
    <a href="#" style="width:97px">Startseite</a><a href="#" style="width:84px">Bestellen</a><a href="#" style="width:78px">Kontakt</a><a href="#" style="width:99px">Impressum</a><a href="#" class="active" style="width:109px">Datenschutz</a><a href="#" style="width:189px">Kredit mit Sofortzusage</a><a href="#" style="width:164px">Schuldnerberatung</a>
  </nav>

  <section class="welcome">
    <h1>Willkommen bei finlo-welt.de</h1>
    <p>Wir nehmen an, dass Sie Schulden haben, denn sonst wären Sie nicht auf dieser Seite gelandet. Die ersten Mahnungen stapeln sich auf Ihrem Schreibtisch und Sie haben keine Ahnung, wie Sie den Schuldenberg wieder abbauen sollen? Ein Banküberfall? Bloß nicht! Es gibt doch legale Tricks, die schon oft funktioniert und den Schuldnern wieder finanziellen Freiraum geschaffen haben.</p>
  </section>

  <div class="cover" role="img" aria-label="Buchcover des eBooks „So befreien Sie sich aus der Schuldenfalle“"></div>

  <section class="help">
    <h2>Wie können wir Ihnen helfen?</h2>
    <p>Mit unserem eBook "So befreien Sie sich aus der Schuldenfalle"! Das eBook enthält die besten Tipps und Tricks um Schulden loszuwerden. Wir erklären Ihnen erst einmal was Schulden sind, wie diese entstehen und vor allem, wie Sie diese wieder los werden. Außerdem gehen wir auch auf Themen wie die Schuldnerberatung, die eidesstattliche Versicherung und die Pfändung ein.</p>
    <p>Sie haben also hiermit ein eBook welches alle Themen die rund um Schulden passieren können abdeckt. Zusätzlich zum eBook "So befreien Sie sich aus der Schuldenfalle" erhalten Sie weitere Informationen. So erfahren Sie, wie Sie Geld sparen können, Geld verdienen können und Sie erhalten nützliche Formulare direkt zum Ausfüllen und ausdrucken.</p>
  </section>
</main>

<aside class="adbox top-label">
  <div class="adlabel"><span>Plunko-Anzeigen</span><span class="go"><svg width="9" height="10"><path d="M1 0 L9 5 L1 10 Z" fill="#fff"/></svg></span></div>
</aside>
<aside class="adbox top-ad" style="left:616px">
  <div class="ad" style="top:0"><div class="ad-title">1. Kredit-Anfrage in 5min</div><div class="ad-text">2. Angebot in Ruhe prüfen 3. auf Wunsch abschließen</div><div class="ad-url">kreditwabe.com/ohneBonvia</div></div>
</aside>
<aside class="adbox top-ad" style="left:817px">
  <div class="ad" style="top:0"><div class="ad-title">1. Kredit-Anfrage in 5min</div><div class="ad-text">2. Angebot in Ruhe prüfen 3. auf Wunsch abschließen</div><div class="ad-url">kreditwabe.com/ohneBonvia</div></div>
</aside>

<aside class="adbox mid">
  <div class="adlabel" style="top:0"><span>Plunko-Anzeigen</span><span class="go"><svg width="9" height="10"><path d="M1 0 L9 5 L1 10 Z" fill="#fff"/></svg></span></div>
  <div class="ad" style="top:34px"><div class="ad-title">1. Kredit-Anfrage in 5min</div><div class="ad-text">2. Angebot in Ruhe prüfen 3. auf Wunsch abschließen</div><div class="ad-url">kreditwabe.com/ohneBonvia</div></div>
  <div class="ad" style="top:161px"><div class="ad-title">Goldene Karte ohne Bonvia</div><div class="ad-text">Echte hochgeprägte Velancard keine Ablehnung möglich! Sofort</div><div class="ad-url">www.karte-morvel.eu</div></div>
</aside>

</body>
</html>
```